Web Design Project

In home dog trainer needs a Web page.
My company is called Tailwise Roaming. I travel to client houses where the owner/handler and I work on any number of dog training ventures determined by the owner/handler in conjunction with myself: Puppy lessons, obedience, leash walking, manners, tricks, frisbee/disc, agility, and flyball.
My logo colour is green and brown.
The final design should communicate a positive in home dog training experience. This needs to feel like something they can accomplish, the process is fun, rewarding and uncomplicated.
I have images to load to the page and some are being ordered of my own dogs in competition and having fun.

Target Market(s)

Home owners, middle to higher income, singles and families

Industry/Entity Type

Dog Training

Requirements
Must have
• The webpage needs to be something I can modify myself in the future as I will be updating information such as where my dogs and I are competing or doing demonstrations, functions we are attending, news appearances, new images. I will also need one page to function as a blog. At the top of the blog or off to one side I would like a small section used as an introduction to who I am. The idea being readers can get an idea as to who I am and how I am qualified to train dogs and then follow the blog.
Another page needs to be for contacting me. Another page needs to list with examples and photos what sort of training I offer: five categories - Cub Launch, Obedience, Manners, Sports.
A facebook link for the future facebook page would also be nice.

Web domain is tailwise-roaming.example

```html
<!DOCTYPE html>
<html lang="en">
<head>
<meta charset="utf-8">
<title>Tailwise Roaming – In Home Dog Training</title>
<link href="https://fonts.googleapis.com/css2?family=Arimo:wght@400;700&display=swap" rel="stylesheet">
<style>
:root{
  --green:#7aab1f;
  --green-light:#d6e2b8;
  --brown:#5a2b08;
  --brown-title:#4b2a12;
  --text:#555;
  --grey-bg:#ececec;
  --footer:#1c1c1c;
  --white:#fff;
}
*{margin:0;padding:0;box-sizing:border-box}
html,body{width:900px;height:1200px;overflow:hidden}
body{position:relative;background:var(--white);font-family:"Arimo",Arial,sans-serif;color:var(--text)}
.abs{position:absolute}
.top-bar{left:0;top:0;width:900px;height:4px;background:var(--green)}
.header{left:0;top:4px;width:900px;height:79px;background:var(--white)}
.brand{left:166px;top:34px;display:flex;align-items:center;gap:6px}
.brand-mark{width:14px;height:14px;border-radius:50%;background:var(--green)}
.brand-name{font-size:15px;font-weight:700;color:var(--green)}
.contact-line{right:166px;top:13px;display:flex;align-items:center;gap:10px;font-size:7.5px;color:#999}
.social-dot{width:10px;height:10px;border-radius:50%;background:#9a9a9a}
.nav{left:394px;top:49px;display:flex;gap:12px;font-size:8.5px;font-weight:700;color:#222}
.nav .active{color:var(--brown);position:relative}
.nav .active::after{content:"";position:absolute;left:-4px;right:-4px;top:26px;height:3px;background:var(--green)}
.hero{left:0;top:83px;width:900px;height:287px;background:linear-gradient(100deg,#6b7a3c 0%,#8fa45a 30%,#c9b48d 50%,#7d9a45 70%,#55702a 100%)}
.hero-arrow{top:124px}
.hero-dots{left:441px;top:274px;display:flex;gap:3px}
.hero-dots span{width:9px;height:9px;border-radius:50%;background:var(--white);border:1px solid #555}
.hero-dots span:first-child{background:#c9b15a}
.hero-band{left:0;top:370px;width:900px;height:4px;background:var(--green)}
.welcome{left:0;top:374px;width:900px;height:144px;background:var(--grey-bg)}
.photo-frame{left:174px;top:18px;width:167px;height:106px;background:var(--white);border:1px solid #ccc;padding:6px}
.photo{width:100%;height:100%}
h1,h2,h3{font-weight:400}
.welcome-title{left:354px;top:30px;font-size:15px;color:var(--brown-title)}
.welcome-text{left:354px;top:53px;width:370px;font-size:7px;line-height:8.6px}
.welcome-text p+p{margin-top:8px}
.section-title{display:flex;align-items:center;gap:8px;font-size:14.5px;color:var(--brown-title)}
.service-title{font-size:14px;color:var(--brown-title)}
.service-text{font-size:7.4px;line-height:8.6px;color:#555}
.read-more{font-size:7px;color:var(--green);display:flex;align-items:center;gap:4px}
.read-more b{font-size:9px;letter-spacing:-1px}
.img-box{border:1px solid #bbb;box-shadow:0 1px 2px rgba(0,0,0,.2)}
.gallery-box{left:181px;top:881px;width:550px;height:111px;border:1px solid #ddd;background:var(--white)}
.thumb{top:17px;width:157px;height:78px;border:1px solid #ccc}
.form-area{left:0;top:1003px;width:900px;height:125px;background:var(--grey-bg);border-top:3px solid var(--green-light)}
.form-title{left:0;width:900px;top:13px;text-align:center;font-size:11.5px;font-weight:700;color:var(--green)}
.form-sub{left:0;width:900px;top:30px;text-align:center;font-size:6.8px;color:#444}
.field{background:var(--white);border:1px solid #ccc;font-size:7px;color:#aaa;padding-left:15px;display:flex;align-items:center}
.quote-btn{left:610px;top:58px;width:120px;height:44px;background:var(--brown);color:var(--white);font-size:8.5px;font-weight:700;display:flex;align-items:center;justify-content:center;box-shadow:0 2px 3px rgba(0,0,0,.3)}
.footer-band{left:0;top:1128px;width:900px;height:4px;background:var(--green)}
.footer{left:0;top:1132px;width:900px;height:68px;background:var(--footer)}
.footer-nav{left:166px;top:31px;display:flex;gap:9px;font-size:6.8px;font-weight:700;color:var(--white)}
.footer-social{left:691px;top:26px;display:flex;gap:8px}
.footer-social span{width:20px;height:20px;border-radius:50%;background:#3d5a9a}
</style>
</head>
<body>
<div class="abs top-bar"></div>

<header class="abs header">
  <div class="abs brand"><span class="brand-mark"></span><span class="brand-name">Tailwise Roaming</span></div>
  <div class="abs contact-line">
    <span>Cell: +1 555 010 4477</span>
    <span class="social-dot"></span><span class="social-dot"></span><span class="social-dot"></span><span class="social-dot"></span><span class="social-dot"></span>
  </div>
  <nav class="abs nav">
    <span class="active">Home</span><span>About Us</span><span>Events</span><span>Pet Portraits</span><span>Agility Shots</span><span>Disc Dog</span><span>Contact Us</span>
  </nav>
</header>

<section class="abs hero" role="img" aria-label="Dog in a grassy field carrying a plastic bottle, another dog leaping at left">
  <svg class="abs hero-arrow" style="left:30px" width="14" height="22" viewBox="0 0 14 22"><path d="M12 2 3 11l9 9" fill="none" stroke="#fff" stroke-width="4"/></svg>
  <svg class="abs hero-arrow" style="left:850px" width="14" height="22" viewBox="0 0 14 22"><path d="m2 2 9 9-9 9" fill="none" stroke="#fff" stroke-width="4"/></svg>
  <div class="abs hero-dots"><span></span><span></span><span></span></div>
</section>
<div class="abs hero-band"></div>

<section class="abs welcome">
  <div class="abs photo-frame"><div class="photo" role="img" aria-label="Trainer signalling a dog jumping over a hurdle" style="background:linear-gradient(180deg,#c4cdd3,#9aa8b0 70%,#4d6a2e)"></div></div>
  <h1 class="abs welcome-title">Welcome To Tailwise Roaming</h1>
  <div class="abs welcome-text">
    <p>Shelterline is a theme for animal shelters with PetHaven Finder built in. Simply drop in your API key and your shelter ID and it will pull in all of your pets and even delete them once they're removed.</p>
    <p>And this area is widgetized and will resize the widgets based on how many you use. It's also styled specifically for both the free and Pro versions of the MailNest Signup plugin.<br>Shelterline is a theme for animal shelters with PetHaven Finder built in. Simply drop in your API key and your shelter ID and it will pull in all of your pets and even delete them once they're removed.</p>
  </div>
</section>

<h2 class="abs section-title" style="left:166px;top:527px">
  <svg width="20" height="28" viewBox="0 0 20 28"><circle cx="6" cy="3" r="2.5" fill="#222"/><path d="M6 6v10l-3 10M6 16l4 10M6 9l6 3" stroke="#222" stroke-width="2.5" fill="none"/><circle cx="15" cy="18" r="2" fill="#222"/></svg>
  Our Services
</h2>

<div class="abs img-box" style="left:181px;top:574px;width:181px;height:108px;background:linear-gradient(180deg,#6d8a4a,#8aa860 50%,#5d8a32)" role="img" aria-label="Grey dog jumping over a training hurdle"></div>
<h3 class="abs service-title" style="left:378px;top:575px">Dog Jumping Training</h3>
<p class="abs service-text" style="left:378px;top:598px;width:354px">Lorem ipsum dolor sit amet, consectetuer adipiscing elit. Morbi commodo, ipsum sed pharetra gravida, orci magna rhoncus neque, id pulvinar odio lorem non turpis. Nullam sit amet enim. Suspendisse id velit vitae ligula volutpat condimentum. Aliquam erat volutpat. Sed quis velit. Nulla facilisi. Nulla libero. Vivamus pharetra posuere sapien.<br>Lorem ipsum dolor sit amet, consectetuer adipiscing elit. Morbi commodo, ipsum sed pharetra gravida, orci magna rhoncus neque, id pulvinar odio lorem non turpis. Nullam sit amet enim. Suspendisse id velit vitae ligula volutpat condimentum. Aliquam erat volutpat. Sed quis velit. Nulla facilisi. Nulla libero. Vivamus pharetra posuere sapien.</p>
<a class="abs read-more" style="left:378px;top:674px">Read More <b>&gt;&gt;</b></a>

<h3 class="abs service-title" style="left:182px;top:714px">Agility</h3>
<p class="abs service-text" style="left:182px;top:737px;width:354px">Lorem ipsum dolor sit amet, consectetuer adipiscing elit. Morbi commodo, ipsum sed pharetra gravida, orci magna rhoncus neque, id pulvinar odio lorem non turpis. Nullam sit amet enim. Suspendisse id velit vitae ligula volutpat condimentum. Aliquam erat volutpat. Sed quis velit. Nulla facilisi. Nulla libero. Vivamus pharetra posuere sapien.<br>Lorem ipsum dolor sit amet, consectetuer adipiscing elit. Morbi commodo, ipsum sed pharetra gravida, orci magna rhoncus neque, id pulvinar odio lorem non turpis. Nullam sit amet enim. Suspendisse id velit vitae ligula volutpat condimentum. Aliquam erat volutpat. Sed quis velit. Nulla facilisi. Nulla libero. Vivamus pharetra posuere sapien.</p>
<a class="abs read-more" style="left:182px;top:811px">Read More <b>&gt;&gt;</b></a>
<div class="abs img-box" style="left:550px;top:717px;width:181px;height:109px;background:linear-gradient(90deg,#2e9a98 0%,#3aa9a0 45%,#c89a50 65%,#5b7a2c)" role="img" aria-label="Golden retriever running out of an agility tunnel"></div>

<h2 class="abs section-title" style="left:167px;top:853px">
  <svg width="14" height="14" viewBox="0 0 14 14"><rect x="1" y="5" width="7" height="7" fill="none" stroke="#222" stroke-width="2"/><rect x="6" y="1" width="7" height="7" fill="#fff" stroke="#222" stroke-width="2"/></svg>
  &nbsp;Gallery
</h2>
<svg class="abs" style="left:701px;top:860px" width="20" height="10" viewBox="0 0 20 10"><path d="M6 1 2 5l4 4M14 1l4 4-4 4" fill="none" stroke="#333" stroke-width="2"/></svg>
<div class="abs gallery-box">
  <div class="abs thumb" style="left:11px;background:linear-gradient(90deg,#3b5a9a,#a06a3a 50%,#6e9a40)" role="img" aria-label="Handler guiding a dog through weave poles"></div>
  <div class="abs thumb" style="left:196px;background:linear-gradient(90deg,#4a4a40,#8a8670 50%,#3e5a30)" role="img" aria-label="White dog weaving between yellow poles"></div>
  <div class="abs thumb" style="left:381px;background:linear-gradient(90deg,#c03030,#7a5a40 50%,#6a9a44)" role="img" aria-label="Spaniel racing through an agility course"></div>
</div>

<section class="abs form-area">
  <h2 class="abs form-title">For More Information</h2>
  <p class="abs form-sub">Fill out the information below and a Tailwise Roaming representative will contact you shortly.</p>
  <div class="abs field" style="left:178px;top:48px;width:129px;height:28px">Name</div>
  <div class="abs field" style="left:320px;top:48px;width:129px;height:28px">Email</div>
  <div class="abs field" style="left:462px;top:48px;width:128px;height:28px">Phone</div>
  <div class="abs field" style="left:178px;top:86px;width:412px;height:28px;padding-left:8px">Comments</div>
  <div class="abs quote-btn">Get quote now</div>
</section>

<div class="abs footer-band"></div>
<footer class="abs footer">
  <nav class="abs footer-nav"><span>Home</span><span>About Us</span><span>Events</span><span>Pet Portraits</span><span>Agility Shots</span><span>Disc Dog</span><span>Contact Us</span></nav>
  <div class="abs footer-social"><span></span><span style="background:#3a7ec0"></span></div>
</footer>
</body>
</html>
```